Gelato Business Card

create a new business card using existing logo

Target Market(s)

B2B

Contact Information for Business Card

typical contact info: logo, address, email, phone, rep name

Colors
0355a3
33a6d7

Requirements
Must have
• a feel of high quality, luxury, happiness
• use cool, comforting color and texture of business card.
Nice to have
• "A Little Perfection Goes A Long Way!" TM
• or, "more quality, more flavor"
• or, "Flavor Matters"

```html
<!DOCTYPE html>
<html lang="en">
<head>
<meta charset="utf-8">
<title>Bellarosa's Artisan Gelato – Business Card</title>
<link href="https://fonts.googleapis.com/css2?family=Lato:wght@400;700&family=Noto+Serif:wght@700&display=swap" rel="stylesheet">
<style>
  :root {
    --backdrop: #2a2a2c;
    --card: #232325;
    --brand: #4a42b8;
    --ink: #f2f2f2;
    --ink-soft: #c9c9cc;
    --rule: #6c6c70;
    --pattern-light: #2e2e31;
    --pattern-dark: #202022;
  }
  * { margin: 0; padding: 0; box-sizing: border-box; }
  html, body {
    width: 1200px; height: 1108px; overflow: hidden;
    background: var(--backdrop);
  }
  .stage {
    position: relative; width: 1200px; height: 1108px;
    display: flex; justify-content: center; align-items: center; gap: 70px;
  }
  .card {
    position: relative; width: 380px; height: 620px;
    background: var(--card);
    border-radius: 22px;
    box-shadow: 0 18px 40px rgba(0,0,0,.45);
    overflow: hidden;
    font-family: "Lato", sans-serif;
    color: var(--ink);
  }
  /* front */
  .card--front { display: flex; flex-direction: column; align-items: center; }
  .brand-mark {
    margin-top: 150px;
    display: flex; align-items: center; gap: 12px;
    font-family: "Lato", sans-serif; font-weight: 700;
    font-size: 30px; letter-spacing: 1px; color: var(--brand);
    text-align: center; line-height: 1.15;
  }
  .brand-mark .dot { width: 18px; height: 18px; border-radius: 50%; background: var(--brand); flex: none; }
  .rep-name { margin-top: 90px; font-size: 25px; font-weight: 400; letter-spacing: .5px; text-transform: uppercase; }
  .rep-title { margin-top: 2px; font-size: 18px; color: var(--ink-soft); }
  .contact-icons {
    margin-top: 18px; width: 210px;
    display: flex; align-items: center; gap: 6px;
  }
  .contact-icons .rule { flex: 1; height: 1px; background: var(--rule); }
  .contact-icons svg { width: 20px; height: 20px; }
  .contact-lines { margin-top: 10px; text-align: center; font-size: 19px; line-height: 1.35; color: var(--ink-soft); }
  .divider { margin: 14px 0 10px; width: 210px; height: 1px; background: var(--rule); }
  .address { text-align: center; font-size: 19px; line-height: 1.35; color: var(--ink-soft); }
  /* back */
  .pattern-field {
    position: absolute; inset: 0;
    background:
      radial-gradient(ellipse at 70% 25%, var(--pattern-light), transparent 60%),
      radial-gradient(ellipse at 30% 60%, var(--pattern-light), transparent 55%),
      linear-gradient(160deg, var(--pattern-light), var(--pattern-dark));
  }
  .brand-mark--small {
    position: absolute; right: 36px; top: 430px; margin: 0;
    font-size: 15px; gap: 7px;
  }
  .brand-mark--small .dot { width: 10px; height: 10px; }
  .tagline {
    position: absolute; left: 0; right: 0; bottom: 48px;
    text-align: center;
    font-family: "Noto Serif", serif; font-weight: 700;
    font-size: 26px; color: #ffffff;
  }
</style>
</head>
<body>
<main class="stage">
  <section class="card card--front">
    <div class="brand-mark"><span class="dot"></span><span>Bellarosa's<br>Artisan Gelato</span></div>
    <h1 class="rep-name">Marco Delvecchio</h1>
    <p class="rep-title">Managing Director</p>
    <div class="contact-icons">
      <span class="rule"></span>
      <svg viewBox="0 0 20 20" aria-label="phone"><circle cx="10" cy="10" r="10" fill="#fff"/><path d="M7 5.5l1.6 2.2-1 1.2c.7 1.4 1.7 2.4 3 3l1.2-1 2.2 1.6-.9 1.8c-3.8-.4-6.6-3.2-7-7z" fill="#232325"/></svg>
      <svg viewBox="0 0 20 20" aria-label="email"><circle cx="10" cy="10" r="10" fill="#fff"/><rect x="5" y="6.5" width="10" height="7" fill="#232325"/><path d="M5 6.5l5 4 5-4" stroke="#fff" stroke-width="1" fill="none"/></svg>
      <svg viewBox="0 0 20 20" aria-label="website"><circle cx="10" cy="10" r="10" fill="#fff"/><circle cx="10" cy="10" r="5" fill="none" stroke="#232325" stroke-width="1.3"/><path d="M5 10h10M10 5c-2 2.8-2 7.2 0 10M10 5c2 2.8 2 7.2 0 10" stroke="#232325" stroke-width="1" fill="none"/></svg>
      <span class="rule"></span>
    </div>
    <p class="contact-lines">444 555 0192<br>hello@bellarosa.com<br>www.bellarosa.com</p>
    <span class="divider"></span>
    <p class="address">18 Harbor Lane, Suite 4,<br>Portland, 97205</p>
  </section>

  <section class="card card--back">
    <div class="pattern-field" role="img" aria-label="Faint repeating brand pattern in dark grey tones"></div>
    <div class="brand-mark brand-mark--small"><span class="dot"></span><span>Bellarosa's</span></div>
    <p class="tagline">More Quality, More Flavor</p>
  </section>
</main>
</body>
</html>
```